Deactivated Coal-Fired Power Plant to be redeveloped into a Green Energy Campus.

Want a striking business card statement that introduces our concept project to provide economic and community recovery to a former rural coal community in western PA.
Essentially 12 project representatives that will lead both the demolition of an existing power plant and the redevelopment to a new Green energy site.
Business Card should reflect our effort.
We are open to ideas.

Target Market(s)

Energy and Power Generation industries

Industry/Entity Type

Power Generation and Data Centers

Contact Information for Business Card

Font styles to use
Sans Serif
Other font styles liked:
• Arial, Calibri

Requirements
Must have
• Multiple colors

```html
<!DOCTYPE html>
<html lang="en">
<head>
<meta charset="utf-8">
<title>Ridgeline Renewal – Business Card</title>
<link rel="stylesheet" href="https://fonts.googleapis.com/css2?family=Roboto:wght@400;700&display=swap">
<style>
  :root {
    --bg: #dcdddf;
    --card: #efefed;
    --green: #12994a;
    --ink: #1a1a1a;
    --grey: #6d6e70;
  }
  * { margin: 0; padding: 0; box-sizing: border-box; }
  html, body { width: 1200px; height: 1051px; overflow: hidden; }
  body {
    background: var(--bg);
    font-family: "Roboto", Arial, sans-serif;
    position: relative;
  }
  .card {
    position: absolute;
    top: 380px;
    width: 510px;
    height: 292px;
    background: var(--card);
    border-bottom: 5px solid var(--green);
    box-shadow: 0 18px 40px rgba(0,0,0,0.18);
  }
  .card--contact { left: 60px; }
  .card--brand { left: 630px; }

  .contact-grid {
    position: absolute;
    top: 92px;
    left: 0;
    right: 0;
    display: flex;
    justify-content: center;
  }
  .identity {
    text-align: right;
    padding-right: 20px;
    padding-top: 4px;
  }
  .identity__name {
    color: var(--green);
    font-weight: 700;
    font-size: 19px;
    letter-spacing: 0.3px;
    text-transform: uppercase;
  }
  .identity__title {
    color: var(--grey);
    font-size: 12.5px;
    margin-top: 4px;
  }
  .divider {
    width: 1.5px;
    background: var(--green);
    height: 96px;
  }
  .details {
    padding-left: 18px;
    font-size: 12.5px;
    color: var(--grey);
  }
  .details__company {
    color: var(--green);
    font-size: 13px;
    margin-bottom: 8px;
  }
  .details__row {
    display: flex;
    align-items: center;
    gap: 7px;
    margin-bottom: 4px;
  }
  .details__row svg { width: 11px; height: 11px; fill: var(--green); flex: none; }

  .brand {
    position: absolute;
    inset: 0;
    display: flex;
    align-items: center;
    justify-content: center;
    gap: 14px;
  }
  .brand__dot {
    width: 46px;
    height: 46px;
    border-radius: 50%;
    background: var(--green);
  }
  .brand__name {
    color: var(--ink);
    font-weight: 700;
    font-size: 30px;
    text-transform: uppercase;
    letter-spacing: 0.5px;
  }
</style>
</head>
<body>
  <section class="card card--contact">
    <div class="contact-grid">
      <div class="identity">
        <p class="identity__name">Daniel Hartwell</p>
        <p class="identity__title">Chief Operating Officer</p>
      </div>
      <div class="divider"></div>
      <div class="details">
        <p class="details__company">Ridgeline Renewal LLC</p>
        <p class="details__row">
          <svg viewBox="0 0 12 12" aria-hidden="true"><path d="M3 0h6a1 1 0 0 1 1 1v10a1 1 0 0 1-1 1H3a1 1 0 0 1-1-1V1a1 1 0 0 1 1-1zm0 1.5v8h6v-8z"/></svg>
          555-014-2280
        </p>
        <p class="details__row">
          <svg viewBox="0 0 12 12" aria-hidden="true"><path d="M2.4 0.6l2 2.2-1 1.3c.7 1.6 1.9 2.8 3.5 3.5l1.3-1 2.2 2-1.2 1.9C5 10.3 1.7 7 0.5 1.8z"/></svg>
          555-014-2280
        </p>
        <p class="details__row">
          <svg viewBox="0 0 12 12" aria-hidden="true"><path d="M0 2.5h12v7H0zM0.8 3.2L6 6.8l5.2-3.6v-.2H0.8z"/></svg>
          dhartwell@ridgelinerenewal.com
        </p>
      </div>
    </div>
  </section>

  <section class="card card--brand">
    <div class="brand">
      <span class="brand__dot"></span>
      <span class="brand__name">Ridgeline Renewal</span>
    </div>
  </section>
</body>
</html>
```